Scientific project description

Here is a project description related to cellular mechanics, showing above the forces acting on cells in the tissues of our body. The forces on single cells are there to depict how forces are acting on cells (pressure squeezes the cell, shear flow is pushing the upward parts of the cell, tension pulls one part of the cell, strain is stretching the whole cell; the single cell images are to be found also on the last page). Intense red/purple are used to indicate that the forces are stressful (the colors to be used do not need to be exactly like these colors). The picture in the middle is a view of cells (same picture on next page if that needs to be modified). At the left, a description of what happens when everything is going well, i.e. the body stays healthy. At the right, if you dysfunction you get disease. Green nuances were used to indicate health, brownish, perhaps not so pleasant nuances were used to indicate disease. Below are the steps of the project.

On the whole, we're rather happy with the concept description as such, but it should look a little bit nicer. To many color nuances give a "noisy" impression, fonts could be nicer, layout more crisp, and the text on the steps should be more readable. We would also like to have two versions of the same picture, one with black background, one with white.

Target Market(s)

Scientists that are evaluating our project

Requirements
Must have
• Easy to grasp the idea, easy to read and understand the underlying idea.
Nice to have
• Would be good to have the Concept title ("Vorlint Concept and Envisioned Project Progression) on top of the figure as indicated in the second brief picture submitted.

```html
<!DOCTYPE html>
<html lang="en">
<head>
<meta charset="utf-8">
<title>Mechanostasis – Concept Overview</title>
<link rel="stylesheet" href="https://fonts.googleapis.com/css2?family=Carlito:ital,wght@0,400;0,700;1,400;1,700&display=swap">
<style>
  :root {
    --bg: #000000;
    --frame-pink: #e4407e;
    --step-pink: #c8285f;
    --step-text: #ffffff;
    --pressure: #e3102a;
    --shear: #ef4a8e;
    --tension: #f7941d;
    --strain: #c12fd2;
    --health: #2b9a36;
    --health-text: #78e25c;
    --disease: #a4501c;
    --disease-text: #f2c08a;
    --frailty-text: #c46a2a;
    --white: #ffffff;
  }
  html, body {
    margin: 0;
    padding: 0;
    width: 1200px;
    height: 1032px;
    overflow: hidden;
    background: var(--bg);
  }
  .concept-canvas {
    display: block;
    width: 1200px;
    height: 1032px;
    font-family: "Carlito", "Calibri", sans-serif;
  }
  .force-ring { fill: none; stroke: var(--frame-pink); stroke-width: 2.5; }
  .force-label { font-style: italic; font-weight: 700; font-size: 23px; text-anchor: middle; }
  .force-label--pressure { fill: var(--pressure); }
  .force-label--shear { fill: var(--shear); }
  .force-label--tension { fill: var(--tension); }
  .force-label--strain { fill: var(--strain); }
  .feed-arrow { fill: var(--bg); stroke: var(--frame-pink); stroke-width: 2.5; stroke-linejoin: miter; }
  .flow-line { stroke: var(--white); stroke-width: 4; fill: none; }
  .flow-head { fill: var(--white); }
  .state-box--health { fill: var(--health); }
  .state-box--disease { fill: var(--disease); }
  .state-box-text { fill: var(--white); font-style: italic; font-weight: 700; font-size: 21px; text-anchor: middle; }
  .outcome--health { fill: var(--health); }
  .outcome--disease { fill: var(--disease); }
  .outcome-text { font-style: italic; font-weight: 700; font-size: 33px; text-anchor: middle; }
  .outcome-text--health { fill: var(--health-text); }
  .outcome-text--disease { fill: var(--disease-text); }
  .path-label { font-size: 26px; }
  .path-label--fitness { fill: var(--health-text); }
  .path-label--frailty { fill: var(--frailty-text); }
  .hub-title { fill: var(--white); font-style: italic; font-weight: 700; font-size: 25px; text-anchor: middle; }
  .steps-frame { fill: none; stroke: var(--frame-pink); stroke-width: 2.5; }
  .steps-pointer { fill: var(--frame-pink); }
  .step-pill { fill: var(--step-pink); }
  .step-text { fill: var(--step-text); font-size: 19px; text-anchor: middle; }
</style>
</head>
<body>
<svg class="concept-canvas" viewBox="0 0 1200 1032" xmlns="http://www.w3.org/2000/svg">
  <defs>
    <radialGradient id="cellViewTone" cx="50%" cy="50%" r="50%">
      <stop offset="0%" stop-color="#2f6a3a"/>
      <stop offset="60%" stop-color="#1d3a26"/>
      <stop offset="88%" stop-color="#0e1a12"/>
      <stop offset="100%" stop-color="#000000"/>
    </radialGradient>
    <radialGradient id="pressureTone"><stop offset="0%" stop-color="#5a0a14"/><stop offset="100%" stop-color="#000"/></radialGradient>
    <radialGradient id="shearTone"><stop offset="0%" stop-color="#4a1630"/><stop offset="100%" stop-color="#000"/></radialGradient>
    <radialGradient id="tensionTone"><stop offset="0%" stop-color="#4d300a"/><stop offset="100%" stop-color="#000"/></radialGradient>
    <radialGradient id="strainTone"><stop offset="0%" stop-color="#3d0f45"/><stop offset="100%" stop-color="#000"/></radialGradient>
    <path id="feedArrowShape" class="feed-arrow" d="M0 -6 L26 -6 L26 -14 L44 0 L26 14 L26 6 L0 6 Z"/>
  </defs>

  <!-- Central cell view -->
  <ellipse cx="600" cy="390" rx="124" ry="96" fill="url(#cellViewTone)" role="img" aria-label="Fluorescence microscopy view of cells with green and red staining"/>

  <!-- Mechanical forces -->
  <g class="force force--pressure">
    <ellipse cx="338" cy="277" rx="99" ry="64" fill="url(#pressureTone)" role="img" aria-label="Cell squeezed flat by downward pressure"/>
    <ellipse class="force-ring" cx="338" cy="277" rx="99" ry="64"/>
    <text class="force-label force-label--pressure" x="320" y="256">Pressure</text>
  </g>
  <g class="force force--shear">
    <ellipse cx="495" cy="180" rx="99" ry="69" fill="url(#shearTone)" role="img" aria-label="Cell pushed sideways by shear flow"/>
    <ellipse class="force-ring" cx="495" cy="180" rx="99" ry="69"/>
    <text class="force-label force-label--shear" x="505" y="146">Shear</text>
  </g>
  <g class="force force--tension">
    <ellipse cx="728" cy="180" rx="99" ry="69" fill="url(#tensionTone)" role="img" aria-label="Cell pulled upward at one point by tension"/>
    <ellipse class="force-ring" cx="728" cy="180" rx="99" ry="69"/>
    <text class="force-label force-label--tension" x="730" y="158">Tension</text>
  </g>
  <g class="force force--strain">
    <ellipse cx="868" cy="289" rx="107" ry="61" fill="url(#strainTone)" role="img" aria-label="Cell stretched end to end by strain"/>
    <ellipse class="force-ring" cx="868" cy="289" rx="107" ry="61"/>
    <text class="force-label force-label--strain" x="868" y="275">Strain</text>
  </g>

  <!-- Hollow arrows feeding the hub -->
  <use href="#feedArrowShape" transform="translate(432 302) rotate(30)"/>
  <use href="#feedArrowShape" transform="translate(545 248) rotate(62)"/>
  <use href="#feedArrowShape" transform="translate(680 248) rotate(118)"/>
  <use href="#feedArrowShape" transform="translate(782 326) rotate(152)"/>

  <text class="hub-title" x="600" y="506">Mechanostasis</text>

  <!-- Health path -->
  <rect class="state-box--health" x="128" y="370" width="164" height="105" rx="6"/>
  <text class="state-box-text" x="210" y="405">Functional</text>
  <text class="state-box-text" x="210" y="430">cellular</text>
  <text class="state-box-text" x="210" y="455">machineries</text>
  <text class="path-label path-label--fitness" x="306" y="396">Cell fitness</text>
  <line class="flow-line" x1="478" y1="422" x2="312" y2="422"/>
  <polygon class="flow-head" points="296,422 314,412 314,432"/>
  <line class="flow-line" x1="210" y1="480" x2="210" y2="502"/>
  <polygon class="flow-head" points="210,514 202,500 218,500"/>
  <ellipse class="outcome--health" cx="210" cy="579" rx="104" ry="53"/>
  <text class="outcome-text outcome-text--health" x="210" y="590">Health</text>

  <!-- Disease path -->
  <rect class="state-box--disease" x="896" y="370" width="170" height="114" rx="6"/>
  <text class="state-box-text" x="981" y="405">Dysfunctional</text>
  <text class="state-box-text" x="981" y="430">cellular</text>
  <text class="state-box-text" x="981" y="455">machineries</text>
  <text class="path-label path-label--frailty" x="757" y="396">Cell Frailty</text>
  <line class="flow-line" x1="894" y1="422" x2="762" y2="422"/>
  <line class="flow-line" x1="760" y1="410" x2="760" y2="434"/>
  <line class="flow-line" x1="981" y1="488" x2="981" y2="502"/>
  <polygon class="flow-head" points="981,514 973,500 989,500"/>
  <ellipse class="outcome--disease" cx="979" cy="579" rx="104" ry="53"/>
  <text class="outcome-text outcome-text--disease" x="979" y="590">Disease</text>

  <!-- Project steps -->
  <rect class="steps-frame" x="349" y="524" width="490" height="336" rx="8"/>
  <polygon class="steps-pointer" points="585,524 615,524 600,512"/>
  <g class="steps">
    <rect class="step-pill" x="530" y="541" width="140" height="28" rx="6"/>
    <text class="step-text" x="600" y="561">Therapies</text>
    <rect class="step-pill" x="521" y="586" width="158" height="28" rx="6"/>
    <text class="step-text" x="600" y="606">Prevention</text>
    <rect class="step-pill" x="510" y="631" width="180" height="28" rx="6"/>
    <text class="step-text" x="600" y="651">Critical targets</text>
    <rect class="step-pill" x="499" y="675" width="202" height="28" rx="6"/>
    <text class="step-text" x="600" y="695">Cellular machineries</text>
    <rect class="step-pill" x="489" y="719" width="222" height="28" rx="6"/>
    <text class="step-text" x="600" y="739">Disease models</text>
    <rect class="step-pill" x="475" y="763" width="250" height="28" rx="6"/>
    <text class="step-text" x="600" y="783">Cell, tissue &amp; organ responses</text>
    <rect class="step-pill" x="461" y="807" width="278" height="28" rx="6"/>
    <text class="step-text" x="600" y="827">Mechanical force models</text>
  </g>
</svg>
</body>
</html>
```